Travel Company is looking for a STAND OUT Business Card

I need a unique Business Card that will truly stand out. Nothing too busy. Simple is good, right? Not looking for a standard design either. No cookie cutter layout. We are a Travel Company that works more with Companies than Travelers. I had an idea to focus and emphasis on the 2 logo a bit more. This is not necessary, however thought it would look interesting. I am just looking for something interesting and a bit different. Does't have to completely off the wall crazy, just not your run of the mill business card.

Target Market(s)

Hoteliers, Resort Management, Call Centers, Executives, Travelers, Families, Businesses

Industry/Entity Type

Hospitality

Contact Information for Business Card

President/CEO - Marcus T Bellamy (title not necessary if design doesn't allow for it)
contact - (407) 555-0186
email - mbellamy@wayfarenow.example
address - 4812 Quillmore Ave #164
Orlando, FL 32804
website - www.wayfarenow.example

Font styles to use
Serif
Other font styles liked:
• Avenir Next LT Pro BOLD

Requirements
Must have
• simple look and design. Unique design
Nice to have
• I attached the 2 logo separate from the main logo. This can be used separately from the Main Logo, together with the main logo or as main logo. I included the logo font. Use it or not, designers choice.
Should not have
• cookie cutter design. Little use of red other than the logo

```html
<!DOCTYPE html>
<html lang="en">
<head>
<meta charset="UTF-8">
<title>Wayfare Now – Business Card</title>
<link href="https://fonts.googleapis.com/css2?family=Roboto:wght@400;700&display=swap" rel="stylesheet">
<style>
  :root {
    --backdrop: #b1b1b1;
    --card-light: #f3f3f3;
    --card-light-edge: #dedede;
    --ink: #0a0a0a;
    --brand-red: #e01e26;
    --paper-text: #ffffff;
  }
  html, body {
    margin: 0;
    padding: 0;
    width: 1200px;
    height: 1050px;
    overflow: hidden;
    background: var(--backdrop);
    font-family: "Roboto", Arial, sans-serif;
  }
  .canvas {
    position: relative;
    width: 1200px;
    height: 1050px;
  }
  .card {
    position: absolute;
    left: 264px;
    width: 672px;
    height: 383px;
    overflow: hidden;
    box-shadow: 0 3px 8px rgba(0,0,0,0.35);
    background: radial-gradient(ellipse at center, #ffffff 0%, var(--card-light) 55%, var(--card-light-edge) 100%);
  }
  .card--front { top: 111px; }
  .card--back { top: 574px; }

  .front-divider {
    position: absolute;
    left: 363px;
    top: 0;
    width: 7px;
    height: 100%;
    background: var(--brand-red);
  }
  .front-panel {
    position: absolute;
    left: 370px;
    top: 0;
    right: 0;
    height: 100%;
    background: var(--ink);
    color: var(--paper-text);
  }
  .contact-name {
    position: absolute;
    left: 48px;
    top: 74px;
    margin: 0;
    font-size: 21px;
    font-weight: 400;
    letter-spacing: 0.2px;
    white-space: nowrap;
  }
  .contact-title {
    position: absolute;
    left: 48px;
    top: 101px;
    margin: 0;
    font-size: 15px;
  }
  .contact-list {
    position: absolute;
    left: 48px;
    top: 154px;
    margin: 0;
    padding: 0;
    list-style: none;
    font-size: 14px;
  }
  .contact-list li {
    display: flex;
    align-items: center;
    height: 19.5px;
    white-space: nowrap;
  }
  .contact-list svg {
    width: 14px;
    height: 14px;
    margin-right: 12px;
    flex: none;
  }
  .contact-address {
    position: absolute;
    left: 48px;
    top: 252px;
    margin: 0;
    font-style: normal;
    font-size: 14px;
    line-height: 19.5px;
    white-space: nowrap;
  }

  .brand {
    position: absolute;
    display: flex;
    align-items: center;
    transform: translate(-50%, -50%);
    white-space: nowrap;
  }
  .brand-dot {
    border-radius: 50%;
    background: var(--brand-red);
    flex: none;
  }
  .brand-name {
    font-weight: 700;
    color: var(--ink);
    letter-spacing: -0.5px;
  }
  .brand--front { left: 175px; top: 191px; }
  .brand--front .brand-dot { width: 26px; height: 26px; margin-right: 12px; }
  .brand--front .brand-name { font-size: 40px; }

  .brand--back { left: 336px; top: 190px; flex-direction: column; }
  .brand--back .brand-dot { width: 96px; height: 96px; margin-bottom: 18px; }
  .brand--back .brand-name { font-size: 30px; }

  .back-rule {
    position: absolute;
    left: 0;
    right: 0;
    top: 344px;
    height: 6px;
    background: var(--brand-red);
  }
  .back-band {
    position: absolute;
    left: 0;
    right: 0;
    top: 350px;
    bottom: 0;
    background: var(--ink);
  }
</style>
</head>
<body>
<main class="canvas">
  <section class="card card--front" aria-label="Card front">
    <div class="brand brand--front">
      <span class="brand-dot"></span>
      <span class="brand-name">Wayfare Now</span>
    </div>
    <div class="front-divider"></div>
    <div class="front-panel">
      <h1 class="contact-name">Marcus T Bellamy</h1>
      <p class="contact-title">President/CEO</p>
      <ul class="contact-list">
        <li>
          <svg viewBox="0 0 16 16" aria-hidden="true"><path fill="#fff" d="M3.6 1.2l2.2 2.6c.3.4.3.9-.1 1.2L4.6 6c.9 2 2.5 3.6 4.5 4.6l1-1.1c.3-.4.9-.4 1.2-.1l2.6 2.2c.4.3.4.9.1 1.3l-1.2 1.4c-.4.4-1 .6-1.6.4C6.2 13.3 2.7 9.8 1.3 4.8c-.2-.6 0-1.2.4-1.6L3 2c.3-.3.4-.7.6-.8z"/></svg>
          (407) 555-0186
        </li>
        <li>
          <svg viewBox="0 0 16 16" aria-hidden="true"><rect x="1" y="3.5" width="14" height="9" fill="none" stroke="#fff" stroke-width="1.4"/><path d="M1 3.5l7 5.5 7-5.5M1 12.5l5-4.5M15 12.5l-5-4.5" fill="none" stroke="#fff" stroke-width="1.2"/></svg>
          mbellamy@wayfarenow.example
        </li>
        <li>
          <svg viewBox="0 0 16 16" aria-hidden="true"><g fill="none" stroke="#fff" stroke-width="1"><circle cx="8" cy="8" r="6.5"/><ellipse cx="8" cy="8" rx="3" ry="6.5"/><path d="M1.5 8h13M2.5 4.8h11M2.5 11.2h11M8 1.5v13"/></g></svg>
          www.wayfarenow.example
        </li>
      </ul>
      <address class="contact-address">
        4812 Quillmore Ave #164<br>
        Orlando, FL 32804
      </address>
    </div>
  </section>

  <section class="card card--back" aria-label="Card back">
    <div class="brand brand--back">
      <span class="brand-dot"></span>
      <span class="brand-name">Wayfare Now</span>
    </div>
    <div class="back-rule"></div>
    <div class="back-band"></div>
  </section>
</main>
</body>
</html>
```